Letterhead and email signature block for school

We are a Remote School in the North West of Western Australia and I want to take our logo and use that to create a professional letter head and email signature block. A sample signature block is attached. For the Letterhead; The logo is also attached. I like the Orange and black combination of the logo, needs to include motto plus the following contact details;
PMB 3 BROOME WA
Phone: (08) 9176 3058
Fax: (08) 9176 3047
ABN: 41 297 580 114

The email signature block needs to have the following;
Devon Lukas Farrow
Principal
Tallowood Creek RCS
Phone: (08) 9176 3058
Fax: (08) 9176 3047
Mobile: 0455 318 207
Email: Devon.Farrow@learnwave.edu.au

Target Market(s)

Parents

Industry/Entity Type

Education

Contact Information for Business Card

Devon Lukas Farrow
Principal
Tallowood Creek RCS
Phone: (08) 9176 3058
Fax: (08) 9176 3047
Mobile: 0455 318 207

Colors
f37122
000000

Requirements
Must have
• see breif

```html
<!DOCTYPE html>
<html lang="en">
<head>
<meta charset="utf-8">
<title>Tallowood Creek RCS – Letterhead and Email Signature</title>
<link rel="stylesheet" href="https://fonts.googleapis.com/css2?family=Open+Sans:wght@400;600;700&family=Roboto+Condensed:wght@700&display=swap">
<style>
  :root {
    --orange: #f37122;
    --black: #000000;
    --ink: #222222;
    --paper: #ffffff;
    --backdrop: #e4e4e4;
    --faint: rgba(0, 0, 0, 0.04);
  }
  html, body {
    margin: 0;
    padding: 0;
    width: 1154px;
    height: 1200px;
    overflow: hidden;
    background: var(--backdrop);
    font-family: "Open Sans", Arial, sans-serif;
    color: var(--ink);
  }
  .stage { position: relative; width: 1154px; height: 1200px; }

  /* Letterhead */
  .letterhead {
    position: absolute;
    left: 297px;
    top: 40px;
    width: 560px;
    height: 792px;
    background: var(--paper);
    box-shadow: 0 6px 18px rgba(0,0,0,0.18);
    overflow: hidden;
  }
  .letterhead__topline {
    position: absolute; top: 0; right: 0;
    width: 62%; height: 5px; background: var(--orange);
  }
  .school-mark {
    display: flex; align-items: center; gap: 8px;
    font-family: "Roboto Condensed", "Arial Narrow", sans-serif;
    font-weight: 700; color: var(--ink);
  }
  .school-mark__square { background: var(--orange); flex: none; }
  .letterhead .school-mark {
    position: absolute; left: 40px; top: 36px; font-size: 17px;
  }
  .letterhead .school-mark__square { width: 14px; height: 14px; }
  .letterhead__contact {
    position: absolute; right: 40px; top: 34px;
    font-size: 10px; line-height: 15px; text-align: left;
  }
  .letterhead__contact .label { color: var(--orange); font-weight: 700; }
  .letterhead__emblem-fade {
    position: absolute; left: 170px; top: 200px; width: 220px; height: 220px;
    border-radius: 50%;
    background: radial-gradient(circle, var(--faint) 0%, rgba(0,0,0,0) 70%);
  }
  .letterhead__footer { position: absolute; left: 0; bottom: 0; width: 560px; height: 40px; }

  /* Email signature */
  .signature {
    position: absolute;
    left: 77px;
    top: 880px;
    width: 1000px;
    height: 240px;
    background: var(--paper);
    box-shadow: 0 6px 18px rgba(0,0,0,0.18);
    overflow: hidden;
  }
  .signature__topline { position: absolute; top: 0; left: 0; width: 100%; height: 8px; background: var(--orange); }
  .signature .school-mark {
    position: absolute; left: 24px; top: 96px; font-size: 20px; width: 170px;
  }
  .signature .school-mark__square { width: 16px; height: 16px; }
  .signature__name {
    position: absolute; left: 210px; top: 50px; margin: 0;
    font-size: 27px; font-weight: 700; color: var(--orange);
  }
  .signature__role { position: absolute; left: 210px; top: 88px; margin: 0; font-size: 20px; }
  .signature__school {
    position: absolute; left: 640px; top: 42px; margin: 0;
    font-family: "Roboto Condensed", "Arial Narrow", sans-serif;
    font-size: 28px; font-weight: 700; color: var(--ink);
  }
  .signature__contacts {
    position: absolute; left: 210px; top: 136px;
    display: grid; grid-template-columns: 210px auto; row-gap: 8px;
    font-size: 17px;
  }
  .signature__contacts .label { color: var(--orange); font-weight: 700; }
  .signature__emblem-fade {
    position: absolute; right: 0; top: 30px; width: 200px; height: 170px;
    background: radial-gradient(circle at 70% 50%, rgba(243,113,34,0.08) 0%, rgba(243,113,34,0) 70%);
  }
  .signature__footer { position: absolute; left: 0; bottom: 0; width: 1000px; height: 40px; }
</style>
</head>
<body>
<main class="stage">

  <section class="letterhead" aria-label="Letterhead">
    <div class="letterhead__topline"></div>
    <div class="school-mark"><span class="school-mark__square"></span>Tallowood Creek RCS</div>
    <address class="letterhead__contact" style="font-style:normal">
      <div>PMB 3 BROOME WA</div>
      <div><span class="label">Phone:</span> (08) 9176 3058</div>
      <div><span class="label">Fax:</span> (08) 9176 3047</div>
      <div><span class="label">ABN:</span> 41 297 580 114</div>
    </address>
    <div class="letterhead__emblem-fade" role="img" aria-label="Faint school emblem watermark"></div>
    <svg class="letterhead__footer" viewBox="0 0 560 40" aria-hidden="true">
      <rect x="0" y="28" width="560" height="6" fill="var(--black)"/>
      <polygon points="360,22 560,22 560,40 342,40" fill="var(--orange)"/>
    </svg>
  </section>

  <section class="signature" aria-label="Email signature">
    <div class="signature__topline"></div>
    <div class="school-mark"><span class="school-mark__square"></span>Tallowood Creek RCS</div>
    <h1 class="signature__name">Devon Lukas Farrow</h1>
    <p class="signature__role">Principal</p>
    <h2 class="signature__school">Tallowood Creek RCS</h2>
    <div class="signature__contacts">
      <div><span class="label">Phone :</span> (08) 9176 3058</div>
      <div><span class="label">Mobile :</span> 0455 318 207</div>
      <div><span class="label">Fax :</span> (08) 9176 3047</div>
      <div><span class="label">Email :</span> Devon.Farrow@learnwave.edu.au</div>
    </div>
    <div class="signature__emblem-fade" role="img" aria-label="Faint school emblem decoration"></div>
    <svg class="signature__footer" viewBox="0 0 1000 40" aria-hidden="true">
      <polygon points="0,22 640,22 626,40 0,40" fill="var(--black)"/>
      <polygon points="680,4 1000,4 1000,40 650,40" fill="var(--orange)"/>
    </svg>
  </section>

</main>
</body>
</html>
```